Brightmoor Paving Stationery Design COMMITTED PAY

We need you to design stationary for a new Business called Brightmoor Paving. We have already got the logo designed and it is attached. Obviously we're looking for a stationery set designed around the colours and style to match the logo.

Use generic name, address, phone, fax, email etc ... I will edit text to required details.

What we need:
- Business Card Design Double Sided (90 x 55m + Bleed 3mm+)
- A4 Letter head Design
- A4 Presentation Folder Design
- Invoice Header Approx 210 x 55mm (Include Logo & Images)

And whatever other bonuses you'd like to kick in associated with the package.

I've attached some images and I've got hundreds more. If you want something else in the way of images, let me know.

I look forward to your seeing your designs.
Updates

Thought I should just clarify the follwoing:

1. The Invoice Header is just a branding for the top of my accounting package form.  It is not contain any contact information or the like.  Just logo, some images and some of your creativity and flair to bring it together.
2. The business does synthetic grass (75% of the business), Wetpour Rubber Surfaces, Softfall Surfaces and Rubber Wood Mulch.  These are categories you might choose to somehow highlight on the letterhead.
3. Business Card reverse side should be used to highlight the categories using images provided.

Wow, I've had some really nice designs submitted thus far, but my concern is that I can't just have an awesome looking card.  I really feel that my card needs to either show or say what we do.  Please make sure your design either shows or says the following:

- Synthetic Grass
- Wetpour Rubber Surfaces
- Softfall Surfaces
- Rubber Wood Mulch
- Shade Structures
- Landscape Structures

Just another note, don't know if I mentioned it or not in the original brief, but I prefer the use of icons instead of text for phone, email, fax etc labels.

Industry/Entity Type

Business

Requirements
Must have
• - Provide full editable source files
- Provide letterhead in MS Word format as well
- All designs must be awesome, but also show or say what we do. This is very important to me. I want anyone to look at our letterhead, business card etc and know instantly what it is that we do.
- Super quick turnaround on handover. I need card files to the printer on Monday morning (that's my Monday at GMT+10)
Nice to have
• - Creative use of the logo for a little bit of wow
Should not have
• - not square, boxy or rigid ... Loosen up a bit!

```html
<!DOCTYPE html>
<html lang="en">
<head>
<meta charset="utf-8">
<title>Brightmoor Paving Letterhead</title>
<link rel="stylesheet" href="https://fonts.googleapis.com/css2?family=Source+Sans+3:wght@400;600;700&display=swap">
<style>
  :root {
    --blue: #1a9cd8;
    --green: #8dc63f;
    --sky: #86d3f3;
    --ink: #2b2b2b;
    --paper: #ffffff;
  }
  html, body {
    margin: 0;
    padding: 0;
    overflow: hidden;
    background: var(--paper);
  }
  .letterhead {
    position: relative;
    width: 927px;
    height: 1200px;
    overflow: hidden;
    background: var(--paper);
    font-family: "Source Sans 3", "Myriad Pro", Arial, sans-serif;
  }
  .service-list {
    position: absolute;
    left: 4px;
    top: 44px;
    width: 140px;
    margin: 0;
    padding: 0;
    list-style: none;
    text-align: center;
    font-size: 11.5px;
    line-height: 14.2px;
  }
  .service-list li:nth-child(odd) { color: var(--blue); }
  .service-list li:nth-child(even) { color: var(--green); }

  .brand {
    position: absolute;
    left: 412px;
    top: 30px;
    display: flex;
    align-items: center;
    gap: 14px;
  }
  .brand-dot {
    width: 66px;
    height: 66px;
    border-radius: 50%;
    background: var(--green);
  }
  .brand-name {
    font-size: 46px;
    font-weight: 700;
    color: var(--blue);
    letter-spacing: 1px;
    text-transform: uppercase;
  }

  .project-photo {
    position: absolute;
    left: 24px;
    width: 99px;
    height: 58px;
    box-shadow: 3px 6px 9px rgba(0,0,0,0.45);
  }
  .photo-path   { top: 207px; background: linear-gradient(160deg, #f2f4ef, #8a9a6b 55%, #5d6a44); }
  .photo-play   { top: 347px; background: linear-gradient(180deg, #e8eef2 0%, #c43a3a 45%, #2f6fc1 75%, #c43a3a); }
  .photo-mascot { top: 486px; background: linear-gradient(135deg, #2a8fcf, #d8b23a 50%, #2a8fcf); }
  .photo-mulch  { top: 644px; background: linear-gradient(160deg, #a04a36, #6d7a48 50%, #7a3325); }
  .photo-lawn   { top: 783px; background: linear-gradient(180deg, #6b6f5e 0%, #5f9e3a 50%, #3f7f2a); }
  .photo-pool   { top: 930px; background: linear-gradient(180deg, #8aa2a8 0%, #4fb0d6 45%, #b06a55 80%); }

  .footer-waves {
    position: absolute;
    left: 0;
    bottom: 0;
    width: 927px;
    height: 200px;
  }
  .contact {
    position: absolute;
    right: 30px;
    top: 1078px;
    text-align: right;
    font-size: 16px;
    line-height: 21px;
    color: var(--ink);
  }
  .contact p { margin: 0; }
  .contact .web {
    margin-top: 5px;
    font-size: 21px;
    color: var(--paper);
  }
</style>
</head>
<body>
<main class="letterhead">
  <ul class="service-list">
    <li>Synthetic Grass</li>
    <li>Wetpour Rubber Surfaces</li>
    <li>Softfall Surfaces</li>
    <li>Rubber Wood Mulch</li>
    <li>Shade Structures</li>
    <li>Landscape Structures</li>
  </ul>

  <header class="brand">
    <span class="brand-dot"></span>
    <span class="brand-name">Brightmoor Paving</span>
  </header>

  <div class="project-photo photo-path" role="img" aria-label="Garden path with stepping stones and planting"></div>
  <div class="project-photo photo-play" role="img" aria-label="Playground with red and blue wetpour rubber surface under shade"></div>
  <div class="project-photo photo-mascot" role="img" aria-label="Cartoon character inlaid in blue rubber surface"></div>
  <div class="project-photo photo-mulch" role="img" aria-label="Garden bed with red rubber wood mulch and plants"></div>
  <div class="project-photo photo-lawn" role="img" aria-label="Backyard laid with synthetic grass"></div>
  <div class="project-photo photo-pool" role="img" aria-label="Pool surrounded by red rubber surfacing"></div>

  <svg class="footer-waves" viewBox="0 1000 927 200" aria-hidden="true">
    <defs>
      <linearGradient id="greenSwoosh" x1="0" y1="0" x2="1" y2="0">
        <stop offset="0" stop-color="#eef6d8"/>
        <stop offset="0.35" stop-color="#c2e07e"/>
        <stop offset="1" stop-color="#8dc63f"/>
      </linearGradient>
    </defs>
    <path d="M0 1098 Q 170 1130 360 1200 L 0 1200 Z" fill="var(--sky)"/>
    <path d="M95 1200 Q 520 1140 927 1022 L 927 1200 Z" fill="url(#greenSwoosh)"/>
  </svg>

  <address class="contact">
    <p>1234 State St.</p>
    <p>City, State 12345</p>
    <p>P: (123) 456-7890</p>
    <p>F: (123-456-7890</p>
    <p class="web">www.brightmoorpaving.com</p>
  </address>
</main>
</body>
</html>
```